Website design for Tallow Ridge Trading Inc

We are looking to build a website for our company. We are a scrap metal recycling company based out of Los Angeles. We purchase scrap metal in the US and ship them to China for recycling into fresh metal ores to supply industrial users. We would designs that emphasize the color green given our name and the nature of our business. Recycling themes are welcomed. We already have a URL at:
http://tallowridgetradinginc.example/
At this point, I would like 4 pages:
- Home page
- About Us
- Resources
- Contact us
Our sister company is Marrow Peak Intl Inc and they have a website that we can use as a starting point.
http://www.marrowpeak-intl.example/
Our competitor has a website below. However we dislike the design given we believe it looks rather dull.
http://www.vesperalloyworks.example/en/
Lastly, this is for a website shell only. Please design the template, graphics, and color schemes. We will write the contents later.

```html
<!DOCTYPE html>
<html lang="en">
<head>
<meta charset="utf-8">
<title>Tallow Ridge Trading Inc – Home</title>
<link rel="stylesheet" href="https://fonts.googleapis.com/css2?family=Arimo:wght@400;700&family=Tinos&display=swap">
<style>
  :root {
    --green-dark: #3f7a0c;
    --green-top: #8fba24;
    --green-mid: #8ab532;
    --green-text: #7fae2a;
    --mint-bg: #e3f1bd;
    --rule: #b9d57e;
    --ink: #444a40;
    --navy: #0f3550;
    --pale: #e8efcc;
    --white: #ffffff;
  }
  * { margin: 0; padding: 0; box-sizing: border-box; }
  html, body { width: 1200px; height: 946px; overflow: hidden; }
  body {
    position: relative;
    background: var(--mint-bg);
    font-family: "Arimo", Arial, sans-serif;
    color: var(--ink);
  }
  .site-header {
    position: absolute; left: 0; top: 0; width: 1200px; height: 123px;
    background: linear-gradient(to bottom, var(--green-top) 0%, #5d9414 55%, #3f7a0c 100%);
  }
  .brand {
    position: absolute; left: 120px; top: 48px;
    display: flex; align-items: center; gap: 12px;
    color: var(--white); font-size: 34px; font-weight: 400; letter-spacing: 0.5px;
  }
  .brand-mark { width: 22px; height: 22px; border-radius: 50%; background: var(--white); }
  .contact { position: absolute; right: 130px; top: 60px; text-align: right; color: var(--white); }
  .phone { display: flex; align-items: center; justify-content: flex-end; gap: 8px; font-size: 25px; line-height: 30px; }
  .email { font-size: 13px; margin-top: 4px; }

  .hero { position: absolute; left: 0; top: 123px; width: 1200px; height: 355px; background: var(--white); border-bottom: 1px solid #9fc25a; }
  .hero-art {
    position: absolute; left: 120px; top: 6px; width: 951px; height: 340px;
    background: linear-gradient(to right, #ffffff 0%, #f3f7e6 30%, #eef4d8 60%, #dcefb8 100%);
  }
  .hero-title { position: absolute; left: 556px; top: 100px; font-family: "Tinos", "Times New Roman", serif; font-size: 35px; font-weight: 400; color: var(--navy); letter-spacing: 0.3px; }
  .hero-text { position: absolute; left: 558px; top: 162px; width: 450px; font-size: 14px; line-height: 16px; color: #222; }
  .hero-arrow { position: absolute; top: 188px; }

  .main-nav { position: absolute; left: 120px; top: 478px; display: flex; gap: 3px; }
  .main-nav a {
    width: 149px; height: 41px; background: var(--green-mid); border-radius: 0 0 6px 6px;
    color: var(--white); font-size: 16.5px; text-decoration: none;
    display: flex; align-items: center; padding-left: 33px; gap: 17px;
  }
  .main-nav a::before { content: ""; width: 11px; height: 11px; border-radius: 50%; background: #dfeac4; }
  .main-nav a.is-current { color: #111; }
  .main-nav a.is-current::before { background: var(--green-dark); }

  .welcome { position: absolute; left: 120px; top: 558px; width: 607px; }
  .welcome h1 { font-size: 25px; font-weight: 400; color: var(--ink); padding-bottom: 1px; border-bottom: 1px solid var(--rule); }
  .welcome h1 span { color: var(--green-text); }
  .welcome-thumb { position: absolute; left: 0; top: 52px; width: 132px; height: 97px; background: linear-gradient(to bottom, #ffffff, #eef6dc); border: 1px solid #d7e6b4; }
  .welcome-intro { position: absolute; left: 144px; top: 50px; width: 460px; font-size: 16.4px; line-height: 25px; }
  .welcome-body { position: absolute; left: 2px; top: 175px; width: 596px; font-size: 16.4px; line-height: 25px; }
  .read-more { position: absolute; left: 516px; top: 280px; width: 90px; height: 26px; background: var(--green-mid); color: var(--white); font-size: 12px; text-align: center; line-height: 26px; text-decoration: none; }

  .side-links { position: absolute; left: 781px; top: 554px; width: 290px; list-style: none; }
  .side-links li { height: 35px; border-bottom: 1px solid var(--rule); display: flex; align-items: center; justify-content: space-between; padding: 8px 2px 0 9px; }
  .side-links a { color: var(--green-text); font-size: 16.4px; text-decoration: none; }

  .site-footer { position: absolute; left: 0; top: 912px; width: 1200px; height: 34px; background: var(--green-dark); color: var(--white); font-size: 12px; }
  .site-footer .domain { position: absolute; left: 121px; top: 15px; }
  .site-footer .rights { position: absolute; right: 130px; top: 13px; }
</style>
</head>
<body>
  <header class="site-header">
    <div class="brand"><span class="brand-mark"></span>Tallow Ridge Trading</div>
    <div class="contact">
      <div class="phone">
        <svg width="29" height="29" viewBox="0 0 29 29" aria-hidden="true"><circle cx="14.5" cy="14.5" r="13" fill="none" stroke="#fff" stroke-width="2"/><path d="M10 8c1 0 2 3 2 4s-1.5 1-1 2 2 3 3 3.5 1-1 2-1 4 1 4 2-1.5 2.5-3 2.5C12 21 8 16 8 11c0-1.5 1-3 2-3z" fill="#fff"/></svg>
        123 456 7890
      </div>
      <div class="email">info@tallowridgetradinginc.example</div>
    </div>
  </header>

  <section class="hero">
    <div class="hero-art" role="img" aria-label="Banner artwork: a light bulb made of leaves, fresh green foliage and a faint recycling emblem"></div>
    <h2 class="hero-title">Good for environment</h2>
    <p class="hero-text">Renew-Halcyn gives a new life to your equipment and work with you to protect our environment.</p>
    <svg class="hero-arrow" style="left:118px" width="36" height="38" aria-hidden="true"><path d="M34 0 L0 19 L34 38 L24 19 Z" fill="var(--pale)"/></svg>
    <svg class="hero-arrow" style="left:1033px" width="36" height="38" aria-hidden="true"><path d="M2 0 L36 19 L2 38 L12 19 Z" fill="var(--pale)"/></svg>
  </section>

  <nav class="main-nav">
    <a href="#" class="is-current">Home</a>
    <a href="#">About Us</a>
    <a href="#">Resources</a>
    <a href="#">Contact Us</a>
  </nav>

  <main class="welcome">
    <h1>Welcome To <span>Our Website</span></h1>
    <div class="welcome-thumb" role="img" aria-label="Green recycling symbol"></div>
    <p class="welcome-intro">We strongly believe in being an honest and trustworthy busi-ness partner to each and every one of our clients. We are committed to always putting our clients' interests first.<br>We are committed to always putting our clients' interests first.</p>
    <p class="welcome-body">We strongly believe in being an honest and trustworthy business partner to each and every one of our clients. We are committed to always putting our clients' interests first.We are committed to always putting our clients' interests first.</p>
    <a class="read-more" href="#">read more</a>
  </main>

  <ul class="side-links">
    <li><a href="#">about the company</a><svg width="18" height="10" aria-hidden="true"><path d="M0 5h16M11 1l5 4-5 4" stroke="#7fae2a" stroke-width="2" fill="none"/></svg></li>
    <li><a href="#">company profile</a><svg width="18" height="10" aria-hidden="true"><path d="M0 5h16M11 1l5 4-5 4" stroke="#7fae2a" stroke-width="2" fill="none"/></svg></li>
    <li><a href="#">green templets for recycle</a><svg width="18" height="10" aria-hidden="true"><path d="M0 5h16M11 1l5 4-5 4" stroke="#7fae2a" stroke-width="2" fill="none"/></svg></li>
    <li><a href="#">about the company</a><svg width="18" height="10" aria-hidden="true"><path d="M0 5h16M11 1l5 4-5 4" stroke="#7fae2a" stroke-width="2" fill="none"/></svg></li>
    <li><a href="#">templets website</a><svg width="18" height="10" aria-hidden="true"><path d="M0 5h16M11 1l5 4-5 4" stroke="#7fae2a" stroke-width="2" fill="none"/></svg></li>
  </ul>

  <footer class="site-footer">
    <span class="domain">tallowridgetradinginc.example</span>
    <span class="rights">All Right Reserved 2013-14.</span>
  </footer>
</body>
</html>
```